Business Card Design Project

We are not a new company, but renamed to "Norvane Kitchens" last year. We specialize in modern high-end cabinetry imports. We would like to communicate a sense of quality and cutting edge technology. Ideally the design would incorporate our logo colors, silver, red and preferably a black, matte background. Though we are open to suggestions.
Logo is attached.
Edit: I have attached rough drafts of the previous cards, this way you will have all necessary content that needs to go on the cards.
Updates
Project Deadline Extended
Reason: We have received a lot of great designs, but due to the sheer number we couldn't respond to all. We will extend the deadline for another 7 days to finalize and provide feedback to designers.
Thank you for your hard work!
Industry/Entity Type
Business
Look and feel
Each slider illustrates characteristics of the customer's brand and the style your logo design should communicate.

```html
<!DOCTYPE html>
<html lang="en">
<head>
<meta charset="utf-8">
<title>Norvane Kitchens — Business Cards</title>
<link href="https://fonts.googleapis.com/css2?family=Montserrat:wght@500;600&family=Oswald:wght@500&family=Open+Sans:wght@400&display=swap" rel="stylesheet">
<style>
  :root {
    --backdrop: #6e4a2e;
    --card-black: #050505;
    --card-charcoal: #1c1d1f;
    --card-charcoal-edge: #0d0d0e;
    --metal-light: rgba(120,121,124,0.85);
    --metal-mid: rgba(60,61,63,0.6);
    --metal-clear: rgba(5,5,5,0);
    --silver: #c9cbcd;
    --silver-light: #eceded;
    --red: #e0262a;
    --info-text: #e6e6e6;
    --label-text: #111111;
  }
  * { margin: 0; padding: 0; box-sizing: border-box; }
  html, body { width: 1200px; height: 788px; overflow: hidden; }
  body {
    position: relative;
    background: var(--backdrop);
    font-family: "Montserrat", sans-serif;
  }
  .side-label {
    position: absolute;
    width: 525px;
    text-align: center;
    font-family: "Open Sans", sans-serif;
    font-size: 20px;
    color: var(--label-text);
  }
  .card {
    position: absolute;
    width: 525px;
    height: 300px;
    border-radius: 20px;
    overflow: hidden;
    box-shadow: 0 4px 10px rgba(0,0,0,0.45);
  }
  .card-front { background: var(--card-black); }
  .card-back {
    background: radial-gradient(ellipse at 50% 40%, var(--card-charcoal) 0%, var(--card-charcoal-edge) 100%);
  }
  .wordmark {
    position: absolute;
    left: 0; right: 0;
    top: 162px;
    text-align: center;
    font-size: 38px;
    font-weight: 600;
    font-variant: small-caps;
    letter-spacing: 1px;
    color: var(--silver);
  }
  .texture {
    position: absolute;
  }
  .texture-top {
    left: 0; top: 0; width: 340px; height: 170px;
    background: radial-gradient(ellipse 58% 68% at 40% 18%, var(--metal-light) 0%, var(--metal-mid) 40%, var(--metal-clear) 100%);
  }
  .texture-bottom {
    right: 0; bottom: 0; width: 300px; height: 140px;
    background: radial-gradient(ellipse 55% 70% at 62% 80%, var(--metal-light) 0%, var(--metal-mid) 40%, var(--metal-clear) 100%);
  }
  .contact {
    position: absolute;
    top: 93px;
    display: flex;
  }
  .identity {
    text-align: right;
    padding-right: 16px;
  }
  .person-name {
    font-size: 15px;
    font-weight: 500;
    letter-spacing: 2px;
    color: var(--red);
    text-transform: uppercase;
    line-height: 20px;
  }
  .person-role {
    font-family: "Oswald", sans-serif;
    font-size: 12px;
    color: var(--silver-light);
    text-transform: uppercase;
    line-height: 18px;
  }
  .details {
    border-left: 2px solid var(--red);
    padding-left: 12px;
    list-style: none;
  }
  .details li {
    display: flex;
    font-size: 12px;
    font-variant: small-caps;
    letter-spacing: 1.4px;
    color: var(--info-text);
    line-height: 20px;
  }
  .details .key { width: 20px; flex: none; }
  .details .value-address { line-height: 18px; padding-top: 1px; }
</style>
</head>
<body>
  <p class="side-label" style="left:50px; top:22px;">front</p>
  <p class="side-label" style="left:625px; top:22px;">front-1</p>
  <p class="side-label" style="left:52px; top:405px;">back</p>
  <p class="side-label" style="left:630px; top:405px;">Back - 1</p>

  <section class="card card-front" style="left:50px; top:62px;">
    <p class="wordmark">Norvane Kitchens</p>
  </section>

  <section class="card card-front" style="left:625px; top:62px;">
    <div class="texture texture-top" role="img" aria-label="Perforated metal texture"></div>
    <div class="texture texture-bottom" role="img" aria-label="Perforated metal texture"></div>
    <p class="wordmark">Norvane Kitchens</p>
  </section>

  <section class="card card-back" style="left:57px; top:447px;">
    <div class="contact" style="left:0; width:525px;">
      <div class="identity" style="width:222px;">
        <p class="person-name">Marek Dovan</p>
        <p class="person-role">President</p>
      </div>
      <ul class="details">
        <li><span class="key">p</span>555.210.0147</li>
        <li><span class="key">f</span>555.210.0148</li>
        <li><span class="key">c</span>555.384.2261</li>
        <li><span class="key">@</span>marek@norvanekitchens.ca</li>
        <li><span class="key">a</span><span class="value-address">1280 - 48 Ave.<br>Calder Ridge, AB T4R 2K9</span></li>
      </ul>
    </div>
  </section>

  <section class="card card-back" style="left:620px; top:447px;">
    <div class="contact" style="left:0; width:525px;">
      <div class="identity" style="width:238px;">
        <p class="person-name">Tobias Dovan</p>
        <p class="person-role">Director</p>
      </div>
      <ul class="details">
        <li><span class="key">p</span>555.210.0147</li>
        <li><span class="key">f</span>555.210.0148</li>
        <li><span class="key">c</span>555.617.9043</li>
        <li><span class="key">@</span>tobias@norvanekitchens.ca</li>
        <li><span class="key">a</span><span class="value-address">1280 - 48 Ave.<br>Calder Ridge, AB T4R 2K9</span></li>
      </ul>
    </div>
  </section>
</body>
</html>
```